Website design for management consulting firm

We need a web design for a new consulting company based in Boston, MA called "Fernhollow Ridge Consulting." This webpage will be simple home page, with a "contact us" page, that describes the services of the consulting firm. The company provides strategic planning, business assessment, process re-designs, and other management consulting functions. I would like the website to look high-tech. A logo was already created via Pixel Harbor.

Target Market(s)

Other business owners across a wide spectrum of industries - from IT to retail.

Industry/Entity Type

It Company

Number of Pages Required

3 page

Colors
0455a3
ffffff

Requirements
Must have
• Front page that provides generic text / overview of the firm. A "services" tab that describes consulting services. A "contact us" tab that provides either a form to contact us or just the contact email address of the company. info@fernhollowridgeconsulting.example

```html
<!DOCTYPE html>
<html lang="en">
<head>
<meta charset="utf-8">
<title>Fernhollow Ridge Consulting</title>
<link rel="stylesheet" href="https://fonts.googleapis.com/css2?family=Open+Sans:ital,wght@0,400;0,600;0,700;1,400&display=swap">
<style>
  :root {
    --brand: #0455a3;
    --brand-dark: #033f7a;
    --white: #ffffff;
    --ink: #222222;
    --body: #555555;
    --muted: #8a8a8a;
    --band: #f4f4f4;
    --footer: #444444;
    --button-dark: #1c1c1c;
  }
  * { box-sizing: border-box; margin: 0; padding: 0; }
  html, body { width: 886px; height: 1200px; overflow: hidden; }
  body {
    position: relative;
    background: var(--white);
    font-family: "Open Sans", Arial, sans-serif;
    color: var(--body);
  }
  .abs { position: absolute; }

  /* Header */
  .site-header { position: absolute; left: 0; top: 0; width: 886px; height: 64px; background: var(--white); border-top: 2px solid var(--brand); box-shadow: 0 1px 2px rgba(0,0,0,.12); z-index: 2; }
  .brand { position: absolute; left: 118px; top: 13px; display: flex; align-items: center; gap: 8px; }
  .brand-mark { width: 34px; height: 36px; background: var(--brand); }
  .brand-name { color: #1a2a3a; font-weight: 600; line-height: 1; }
  .brand-name .line1 { display: block; font-size: 18px; letter-spacing: -0.3px; }
  .brand-name .line2 { display: block; font-size: 8px; margin-top: 3px; }
  .main-nav { position: absolute; left: 351px; top: 0; height: 62px; display: flex; }
  .main-nav a { display: flex; align-items: center; padding: 0 16px; font-size: 8.5px; font-weight: 700; color: #222; text-decoration: none; }
  .main-nav a.active { background: var(--brand); color: var(--white); padding: 0 15px; }

  /* Hero */
  .hero { position: absolute; left: 0; top: 64px; width: 886px; height: 382px; background: linear-gradient(100deg, #e6e4e0 0%, #d8d3cc 30%, #8f98a6 55%, #3d4e6a 75%, #2a3650 100%); }
  .slider-arrow { position: absolute; top: 165px; width: 36px; height: 53px; }
  .slider-arrow.prev { left: 0; background: rgba(90,90,90,.6); }
  .slider-arrow.next { right: 0; background: rgba(25,35,55,.85); }
  .quick-form { position: absolute; left: 119px; top: 75px; width: 177px; height: 235px; background: var(--brand); box-shadow: 0 2px 6px rgba(0,0,0,.25); }
  .quick-form h2 { position: absolute; left: 0; top: 10px; width: 100%; text-align: center; font-size: 12px; font-weight: 700; color: var(--white); }
  .quick-form .rule { position: absolute; left: 15px; top: 27px; width: 147px; height: 1px; background: rgba(255,255,255,.35); }
  .field { position: absolute; left: 15px; width: 148px; height: 19px; background: var(--white); font-size: 6.5px; color: var(--muted); padding: 5px 5px; }
  .field.message { height: 53px; }
  .field .caret { position: absolute; right: 4px; top: 7px; width: 0; height: 0; border-left: 3px solid transparent; border-right: 3px solid transparent; border-top: 4px solid #444; }
  .submit-btn { position: absolute; left: 15px; top: 201px; width: 83px; height: 24px; background: var(--button-dark); color: var(--white); font-size: 8.5px; font-weight: 600; display: flex; align-items: center; justify-content: center; border-radius: 2px; }

  /* Welcome */
  .welcome-title { position: absolute; left: 0; top: 466px; width: 886px; text-align: center; font-size: 15px; font-weight: 600; color: var(--ink); }
  .welcome-sub { position: absolute; left: 0; top: 492px; width: 886px; text-align: center; font-size: 10px; font-style: italic; color: var(--brand); }
  .welcome-text { position: absolute; left: 218px; top: 520px; width: 450px; text-align: center; font-size: 7.6px; line-height: 13.6px; color: var(--body); }

  /* Services */
  .services-band { position: absolute; left: 0; top: 580px; width: 886px; height: 309px; background: var(--band); }
  .section-title { position: absolute; font-size: 14.5px; font-weight: 600; color: var(--ink); }
  .service-card { position: absolute; top: 634px; width: 150px; }
  .service-photo { width: 150px; height: 116px; box-shadow: 0 4px 5px -3px rgba(0,0,0,.35); }
  .service-card h3 { margin-top: 14px; font-size: 10.4px; font-weight: 600; color: var(--brand); line-height: 14px; }
  .service-card p { margin-top: 8px; font-size: 7.6px; line-height: 13.6px; color: var(--body); }
  .read-btn { position: absolute; top: 204px; left: 0; width: 66px; height: 26px; background: var(--brand); color: var(--white); font-size: 7.6px; display: flex; align-items: center; justify-content: center; }

  /* Events / What we do */
  .split-title { position: absolute; top: 910px; font-size: 11.5px; font-weight: 700; color: #333; }
  .split-title span { color: var(--brand); }
  .event-photo { position: absolute; left: 118px; width: 102px; height: 83px; }
  .event-body { position: absolute; left: 236px; width: 196px; }
  .event-date { font-size: 9px; font-weight: 600; color: var(--brand); }
  .event-body p { margin-top: 6px; font-size: 7.6px; line-height: 13.4px; color: var(--body); }
  .event-body a { display: block; margin-top: 4px; margin-left: 2px; font-size: 7.6px; color: var(--brand); text-decoration: none; }
  .work-photo { position: absolute; top: 945px; width: 149px; height: 103px; }
  .work-sub { position: absolute; left: 457px; top: 1061px; font-size: 10.3px; color: var(--brand); }
  .work-text { position: absolute; left: 457px; top: 1085px; width: 315px; font-size: 7.6px; line-height: 13.4px; color: var(--body); }

  /* Footer */
  .site-footer { position: absolute; left: 0; top: 1156px; width: 886px; height: 44px; background: var(--footer); }
  .social { position: absolute; left: 118px; top: 9px; display: flex; gap: 6px; }
  .social span { width: 26px; height: 26px; border: 1.6px solid var(--white); border-radius: 50%; }
  .copyright { position: absolute; right: 120px; top: 16px; font-size: 7.6px; color: #eeeeee; }
</style>
</head>
<body>

<header class="site-header">
  <div class="brand">
    <div class="brand-mark"></div>
    <div class="brand-name"><span class="line1">Fernhollow Ridge</span><span class="line2">Consulting</span></div>
  </div>
  <nav class="main-nav">
    <a class="active" href="#">HOME</a>
    <a href="#">ABOUT US</a>
    <a href="#">SERVICES</a>
    <a href="#">HOW IT WORKS</a>
    <a href="#">FAQ</a>
    <a href="#">CONTACT US</a>
  </nav>
</header>

<section class="hero" role="img" aria-label="Photo of two businessmen in suits reviewing a tablet at a meeting table">
  <div class="slider-arrow prev">
    <svg width="36" height="53" viewBox="0 0 36 53"><polyline points="21,14 10,26.5 21,39" fill="none" stroke="#fff" stroke-width="1.4"/></svg>
  </div>
  <div class="slider-arrow next">
    <svg width="36" height="53" viewBox="0 0 36 53"><polyline points="15,14 26,26.5 15,39" fill="none" stroke="#fff" stroke-width="1.4"/></svg>
  </div>
  <form class="quick-form">
    <h2>QUICK CONTACT FORM</h2>
    <div class="rule"></div>
    <div class="field" style="top:37px">Name:</div>
    <div class="field" style="top:63px">Email*</div>
    <div class="field" style="top:88px">Phone*</div>
    <div class="field" style="top:113px">Services<span class="caret"></span></div>
    <div class="field message" style="top:138px">Message</div>
    <div class="submit-btn">SUBMIT HERE</div>
  </form>
</section>

<h1 class="welcome-title">WELCOME! TO &nbsp;FERNHOLLOW RIDGE CONSULTING</h1>
<p class="welcome-sub">Sed ut perspiciatis unde omnis iste natus error sit voluptatem acc usantium dolor</p>
<p class="welcome-text">Sed ut perspiciatis unde omnis iste natus error sit voluptatem accusantium doloremque laudantium, totam rem aperiam, eaque ipsa quae ab illo inventore veritatis et quasi architecto beatae vitae dicta sunt explicabo. Nemo enim ipsam voluptatem quia voluptas sit aspernatur aut odit aut fugit, sed quia consequuntur magni dolores eos qui ratione.</p>

<section class="services-band"></section>
<h2 class="section-title" style="left:118px; top:602px">OUR SERVICES</h2>

<article class="service-card" style="left:118px">
  <div class="service-photo" role="img" aria-label="Photo of a desk with charts, glasses and a coffee cup" style="background:linear-gradient(135deg,#8a6a48,#c9a27a 50%,#6d5a46)"></div>
  <h3>STRATEGIC PLANNING</h3>
  <p>Sed ut perspiciatis unde omnis iste natus error sit voluptatem accusantium doloremque laudantium, totacon.</p>
  <a class="read-btn" href="#">READ MORE</a>
</article>
<article class="service-card" style="left:285px">
  <div class="service-photo" role="img" aria-label="Photo of a hand touching a tablet showing data charts" style="background:linear-gradient(135deg,#5f7fa8,#c8d8ea 50%,#7e97b8)"></div>
  <h3>BUSINESS ASSESSMENT</h3>
  <p>Sed ut perspiciatis unde omnis iste natus error sit voluptatem accusantium doloremque laudantium, totacon.</p>
  <a class="read-btn" href="#">READ MORE</a>
</article>
<article class="service-card" style="left:451px">
  <div class="service-photo" role="img" aria-label="Photo of hands with pens over printed reports" style="background:linear-gradient(135deg,#6c6c6c,#e2e2e2 55%,#a9a9a9)"></div>
  <h3>PROCESS RE-DESIGNS</h3>
  <p>Sed ut perspiciatis unde omnis iste natus error sit voluptatem accusantium doloremque laudantium, totacon.</p>
  <a class="read-btn" href="#">READ MORE</a>
</article>
<article class="service-card" style="left:618px">
  <div class="service-photo" role="img" aria-label="Photo of business people meeting at a table" style="background:linear-gradient(135deg,#d9d9d9,#7b7b7b 50%,#2e2e35)"></div>
  <h3>OTHER MANAGEMENT<br>CONSULTING FUNCTIONS</h3>
  <p>Sed ut perspiciatis unde omnis iste natus error sit voluptatem accusantium</p>
  <a class="read-btn" href="#">READ MORE</a>
</article>

<h2 class="split-title" style="left:120px">UPCOMING <span>EVENTS</span></h2>
<h2 class="split-title" style="left:457px">WHAT <span>WE DO</span></h2>

<div class="event-photo" style="top:945px; background:linear-gradient(135deg,#4d6a80,#b7c3cc 55%,#6e7d88)" role="img" aria-label="Photo of a business presentation"></div>
<div class="event-body" style="top:944px">
  <div class="event-date">Oct 20 2015</div>
  <p>Lorem ipsum dolor sit amet, consectetur adipiscing elit, sed do eiusmod tempor incididunt ut labore et dolore magna aliquat enim ad minim</p>
  <a href="#">Read More</a>
</div>

<div class="event-photo" style="top:1046px; background:linear-gradient(135deg,#0b1a3a,#1f4f9a 55%,#07112a)" role="img" aria-label="Photo of a businessman touching a glowing financial chart"></div>
<div class="event-body" style="top:1045px">
  <div class="event-date">Oct 20 2015</div>
  <p>Lorem ipsum dolor sit amet, consectetur adipiscing elit, sed do eiusmod tempor incididunt ut labore et dolore magna aliquat enim ad minim</p>
  <a href="#">Read More</a>
</div>

<div class="work-photo" style="left:457px; background:linear-gradient(135deg,#2a2a2a,#9a9a9a 55%,#d8d8d8)" role="img" aria-label="Photo of a businesswoman in a meeting"></div>
<div class="work-photo" style="left:618px; background:linear-gradient(135deg,#c9c9c9,#7a6a5e 55%,#e0e0e0)" role="img" aria-label="Photo of a businesswoman holding a tablet in an office"></div>
<p class="work-sub">Sed ut perspiciatis unde omnis iste natus error sit</p>
<p class="work-text">Sed ut perspiciatis unde omnis iste natus error sit voluptatem accusantium dolor emque laudantium, totam rem aperiam, eaque ipsa quae ab illo inventore veritatis et quasi architecto beatae vitae dicta sunt explicabo.</p>

<footer class="site-footer">
  <div class="social" aria-label="Social links">
    <span></span><span></span><span></span><span></span>
  </div>
  <p class="copyright">© 2015 all copyrights are reserved. Fernhollow Ridge Consulting</p>
</footer>

</body>
</html>
```